Vira Glow - Letter Head

My company is a residential and commercial cleaning company , which is located in Abu Dhabi, UAE.
I am looking for a creative letterhead reflects the professional and reflects professionalism and send the feeling of relax and comfort.
The color which will be used it has to be selected carefully in prospective of colors psychological effects, so every color to be used should be for a reason.
Also, reflecting my company colors in an attractive way.
Regarding the information which it should contains, it has to show the address, contacts , telephones an, email address and website.
Also, my company logo is attached

```html
<!DOCTYPE html>
<html lang="en">
<head>
<meta charset="utf-8">
<title>Vira Glow – Letterhead</title>
<link href="https://fonts.googleapis.com/css2?family=Nunito:wght@400;600;800&display=swap" rel="stylesheet">
<style>
  :root {
    --paper: #ffffff;
    --brand-blue: #1f72b8;
    --brand-green: #a9cf45;
    --soft-green: #c7dd87;
    --soft-blue: #7fa6d6;
    --mark-grey: #d8d9da;
    --text-grey: #5b6470;
  }
  html, body {
    margin: 0;
    padding: 0;
    overflow: hidden;
    background: var(--paper);
  }
  .letterhead {
    position: relative;
    width: 848px;
    height: 1200px;
    background: var(--paper);
    overflow: hidden;
    font-family: "Nunito", sans-serif;
  }
  .brand {
    position: absolute;
    left: 52px;
    top: 72px;
    display: flex;
    align-items: center;
    gap: 16px;
  }
  .brand-name {
    font-weight: 800;
    font-size: 40px;
    line-height: 40px;
    color: var(--brand-blue);
    margin: 0;
  }
  .brand-dot {
    width: 100px;
    height: 100px;
    border-radius: 50%;
    border: 5px solid var(--brand-green);
    box-sizing: border-box;
  }
  .contact {
    position: absolute;
    right: 52px;
    top: 82px;
    margin: 0;
    padding: 0;
    list-style: none;
    text-align: right;
    font-size: 13px;
    line-height: 21px;
    font-weight: 400;
    color: var(--text-grey);
  }
  .contact-label {
    font-weight: 600;
    color: var(--brand-blue);
    margin-right: 6px;
  }
  .background-mark {
    position: absolute;
    left: 226px;
    top: 392px;
    width: 480px;
    height: 480px;
    border-radius: 50%;
    border: 14px solid var(--mark-grey);
    box-sizing: border-box;
    display: flex;
    align-items: center;
    justify-content: center;
  }
  .background-mark span {
    font-weight: 800;
    font-size: 64px;
    color: var(--mark-grey);
  }
  .footer-waves {
    position: absolute;
    left: 0;
    top: 1100px;
    width: 848px;
    height: 100px;
  }
</style>
</head>
<body>
  <main class="letterhead">
    <header class="brand">
      <h1 class="brand-name">Vira<br>Glow</h1>
      <div class="brand-dot" aria-hidden="true"></div>
    </header>

    <ul class="contact">
      <li><span class="contact-label">Address</span>Office 204, Al Noor Tower, Abu Dhabi, UAE</li>
      <li><span class="contact-label">Tel</span>+971 2 555 0148 &nbsp;|&nbsp; +971 50 555 0192</li>
      <li><span class="contact-label">Email</span>info@viraglow.example</li>
      <li><span class="contact-label">Web</span>www.viraglow.example</li>
    </ul>

    <div class="background-mark" aria-hidden="true"><span>Vira Glow</span></div>

    <svg class="footer-waves" viewBox="0 1100 848 100" aria-hidden="true">
      <path class="wave-blue" fill="var(--soft-blue)"
            d="M0 1134 C150 1160 400 1152 600 1124 C700 1112 800 1128 848 1148
               L848 1150 C700 1132 520 1142 380 1158 C240 1172 100 1176 0 1170 Z"/>
      <path class="wave-green" fill="var(--soft-green)"
            d="M0 1172 C120 1178 260 1172 400 1160 C540 1148 700 1136 848 1152
               L848 1200 L0 1200 Z"/>
    </svg>
  </main>
</body>
</html>
```